Rainbow card

Looking for someone to design a card using rainbow theme and link 7 different promises of love to each color. The design will be used to either print a greeting card for valentines or flyer type layout to be framed.

Target Market(s)

Personal

Font styles to use
Script

Colors
eb1f27
f78f20
faee3e
9bcb3c
0655a3
6a429a
a64599

Requirements
Must have
• Rainbow
• The phrases to be included on each color are:
• red - I'll never leave you as long as you'll have me.
• orange - I'll never deny you my body.
• yellow - I'll never let you go to prison.
• green - I'll have a baby with you.
• blue - I'll marry you.
• Indigo - I'll always love you.
• Violet - I'll always stand by you and support you.
Nice to have
• Rainbow, love and loyalty significance

```html
<!DOCTYPE html>
<html lang="en">
<head>
<meta charset="utf-8">
<title>Seven Promises Rainbow Card</title>
<link href="https://fonts.googleapis.com/css2?family=Dancing+Script:wght@700&display=swap" rel="stylesheet">
<style>
  :root {
    --paper: #ffffff;
    --red: #eb1f27;
    --orange: #f78f20;
    --yellow: #faee3e;
    --green: #9bcb3c;
    --blue: #0655a3;
    --indigo: #6a429a;
    --violet: #a64599;
    --ink-light: #ffffff;
    --ink-warm: #8a5a00;
  }
  html, body {
    margin: 0;
    padding: 0;
    width: 1200px;
    height: 968px;
    overflow: hidden;
    background: var(--paper);
  }
  .card {
    display: block;
    width: 1200px;
    height: 968px;
  }
  .band--red { fill: var(--red); }
  .band--orange { fill: var(--orange); }
  .band--yellow { fill: var(--yellow); }
  .band--green { fill: var(--green); }
  .band--blue { fill: var(--blue); }
  .band--indigo { fill: var(--indigo); }
  .band--violet { fill: var(--violet); }
  .promise {
    font-family: "Dancing Script", cursive;
    font-weight: 700;
    fill: var(--ink-light);
    text-anchor: middle;
  }
  .promise--red { font-size: 34px; }
  .promise--orange { font-size: 34px; }
  .promise--yellow { font-size: 32px; fill: var(--ink-warm); }
  .promise--green { font-size: 30px; }
  .promise--blue { font-size: 28px; }
  .promise--indigo { font-size: 24px; }
  .promise--violet { font-size: 19px; }
</style>
</head>
<body>
<svg class="card" viewBox="0 0 1200 968" xmlns="http://www.w3.org/2000/svg">
  <defs>
    <path id="line-red" d="M167 680 A433 433 0 0 1 1033 680"/>
    <path id="line-orange" d="M219 680 A381 381 0 0 1 981 680"/>
    <path id="line-yellow" d="M270 680 A330 330 0 0 1 930 680"/>
    <path id="line-green" d="M322 680 A278 278 0 0 1 878 680"/>
    <path id="line-blue" d="M373 680 A227 227 0 0 1 827 680"/>
    <path id="line-indigo" d="M424 680 A176 176 0 0 1 776 680"/>
    <path id="line-violet" d="M474 680 A126 126 0 0 1 726 680"/>
  </defs>

  <g class="rainbow-bands">
    <path class="band--red" d="M130 680 A470 470 0 0 1 1070 680 L1018 680 A418 418 0 0 0 182 680 Z"/>
    <path class="band--orange" d="M182 680 A418 418 0 0 1 1018 680 L966 680 A366 366 0 0 0 234 680 Z"/>
    <path class="band--yellow" d="M234 680 A366 366 0 0 1 966 680 L914 680 A314 314 0 0 0 286 680 Z"/>
    <path class="band--green" d="M286 680 A314 314 0 0 1 914 680 L862 680 A262 262 0 0 0 338 680 Z"/>
    <path class="band--blue" d="M338 680 A262 262 0 0 1 862 680 L810 680 A210 210 0 0 0 390 680 Z"/>
    <path class="band--indigo" d="M390 680 A210 210 0 0 1 810 680 L758 680 A158 158 0 0 0 442 680 Z"/>
    <path class="band--violet" d="M442 680 A158 158 0 0 1 758 680 L706 680 A106 106 0 0 0 494 680 Z"/>
  </g>

  <g class="promises">
    <text class="promise promise--red"><textPath href="#line-red" startOffset="50%">I'll never leave you as long as you'll have me.</textPath></text>
    <text class="promise promise--orange"><textPath href="#line-orange" startOffset="50%">I'll never deny you my body.</textPath></text>
    <text class="promise promise--yellow"><textPath href="#line-yellow" startOffset="50%">I'll never let you go to prison.</textPath></text>
    <text class="promise promise--green"><textPath href="#line-green" startOffset="50%">I'll have a baby with you.</textPath></text>
    <text class="promise promise--blue"><textPath href="#line-blue" startOffset="50%">I'll marry you.</textPath></text>
    <text class="promise promise--indigo"><textPath href="#line-indigo" startOffset="50%">I'll always love you.</textPath></text>
    <text class="promise promise--violet"><textPath href="#line-violet" startOffset="50%">I'll always stand by you and support you.</textPath></text>
  </g>
</svg>
</body>
</html>
```